Rug Cleaning Web Design Project

We need a web design for our cleaning company. We currently have a web page but are not happy with its design. We currently offer fine rug cleaning,upholstery cleaning, and residential and commercial carpet cleanning. We also offer water damage restoration. For our rug cleaning services we offer : Enzyme treatments for pet contamination and odor removal, application of stain protection that is designed for the fine textiles used in rug construction, application of treatments designed to prevent moth damage and pads designed to be used under rugs.Our current web site is harborfreshcare.example. We are intrested in a design with similar information to the web page of Velmora Rug Cleaners INC. We would like to use the colors that are present in our logo that will be uploaded with this description. We would also like this new page to be linked to our other address loomrinsepro.example. We would like the deign to be visually attractive but not "too busy".
Updates

Please include pictures of rugs, or people washing rugs if possible. We do not offer maid type cleaning services. We would not be interested in designs including pictures depicting that type service. Thanks for your hard work on this project.

Dana Whitlow

Industry/Entity Type

Residential

Requirements
Must have
• This page must be viewable on smart phones and tablets.

```html
<!DOCTYPE html>
<html lang="en">
<head>
<meta charset="utf-8">
<title>Loom Rinse Pro – Rug Cleaning</title>
<link rel="stylesheet" href="https://fonts.googleapis.com/css2?family=Open+Sans:wght@400;600;700&family=Courgette&display=swap">
<style>
:root{
  --brand-blue:#1f8fc9;
  --brand-blue-light:#4fb3e3;
  --brand-blue-dark:#1674a8;
  --nav-active:#3b3f44;
  --accent-red:#d62f2f;
  --ink:#333;
  --ink-soft:#555;
  --page:#f7f7f5;
  --footer:#1f1f1f;
  --footer-text:#cfcfcf;
  --footer-head:#5fb6e6;
}
*{box-sizing:border-box;margin:0;padding:0}
html,body{width:1200px;height:1125px;overflow:hidden}
body{position:relative;background:var(--page);font-family:"Open Sans",Arial,sans-serif;color:var(--ink)}
.header{position:absolute;left:0;top:0;width:1200px;height:94px;background:#fff}
.brand{position:absolute;left:130px;top:26px;display:flex;align-items:center;gap:12px}
.brand-dot{width:40px;height:40px;border-radius:50%;background:var(--brand-blue)}
.brand-name{font-size:34px;font-weight:700;color:#2b2f33;letter-spacing:-0.5px}
.call{position:absolute;left:826px;top:10px;display:flex;align-items:center;gap:9px;font-size:12px;color:#666}
.call-icon{width:21px;height:21px;border-radius:4px;background:var(--accent-red);display:flex;align-items:center;justify-content:center}
.call strong{font-size:17px;font-weight:400;color:#444;margin-left:4px}
.nav{position:absolute;left:545px;top:46px;width:523px;height:36px;display:flex;background:linear-gradient(#4db1e2,#1f8fc9);box-shadow:0 2px 3px rgba(0,0,0,.25)}
.nav a{flex:auto;display:flex;align-items:center;justify-content:center;color:#fff;text-decoration:none;font-size:15px;border-right:1px solid rgba(255,255,255,.25)}
.nav a.active{background:linear-gradient(#53585e,#2f3337);flex:0 0 95px}
.hero{position:absolute;left:0;top:94px;width:1200px;height:526px;background:linear-gradient(180deg,#5a4d44 0%,#9a8a7a 35%,#d8cbb8 62%,#c9b69b 78%,#efece7 100%)}
.thumbs{position:absolute;left:134px;top:535px;display:flex;gap:13px}
.thumb{position:relative;width:80px;height:78px;border:3px solid #fff;box-shadow:0 1px 3px rgba(0,0,0,.35)}
.thumb.current::before{content:"";position:absolute;left:28px;top:-16px;border:12px solid transparent;border-bottom-color:#fff}
.t1{background:linear-gradient(#cfd3d6,#7f8488)}
.t2{background:linear-gradient(#c7b295,#8b7459)}
.t3{background:linear-gradient(#b9bcc4,#5b6d93)}
.t4{background:linear-gradient(#bfd3e6,#a79a7c)}
.intro{position:absolute;left:134px;top:660px;width:638px}
.intro h1{font-size:17px;font-weight:400;color:var(--accent-red);padding-bottom:8px;border-bottom:1px dashed #bbb}
.intro h2{font-family:"Courgette",cursive;font-weight:400;font-size:20px;line-height:26px;color:#333;margin:16px 0 10px}
.intro p{font-family:Arial,sans-serif;font-size:12px;line-height:16px;color:var(--ink-soft);margin-bottom:16px}
.services{position:absolute;left:830px;top:643px;width:238px;height:265px;background:linear-gradient(#3fa3d8,#2a8fc6);box-shadow:0 2px 4px rgba(0,0,0,.25);color:#fff}
.services-rings{position:absolute;left:8px;top:-5px;width:222px;display:flex;justify-content:space-between}
.services-rings span{width:10px;height:10px;border-radius:50%;border:2px solid #1c6e9b;background:#8fd0f0}
.services h3{font-weight:400;font-size:17px;text-align:center;margin-top:24px;padding-bottom:16px;border-bottom:1px solid rgba(255,255,255,.35);margin-left:14px;margin-right:14px}
.services ul{list-style:none;margin:14px 0 0 26px}
.services li{font-size:14px;height:33px;display:flex;align-items:center;gap:8px}
.services li::before{content:"";width:7px;height:7px;border-radius:50%;background:#fff}
.footer{position:absolute;left:0;top:943px;width:1200px;height:182px;background:var(--footer);color:var(--footer-text);font-size:11px}
.footer-col{position:absolute;top:30px}
.footer h4{font-weight:400;font-size:14px;color:var(--footer-head);margin-bottom:12px}
.footer ul{list-style:none}
.footer li{height:22px;display:flex;align-items:center;gap:8px}
.bullet::before{content:"";width:5px;height:5px;border-radius:50%;background:#ddd}
.social-box{width:13px;height:13px;border-radius:2px;background:#5a6f8f}
.testimonial{width:140px;line-height:16px;color:#aaa;position:relative;padding-left:10px}
.testimonial::before{content:"\201C";position:absolute;left:-8px;top:-6px;font-size:24px;color:#777}
.testimonial::after{content:"\201D";position:absolute;right:-16px;bottom:-12px;font-size:24px;color:#777}
.author{color:var(--accent-red);margin-top:20px}
.contact p{display:flex;gap:10px;width:210px;line-height:15px;margin-bottom:10px}
.contact svg{flex:none;margin-top:2px}
.marker{position:absolute;left:1006px;top:-1px;border:8px solid transparent;border-top-color:var(--page)}
</style>
</head>
<body>
<header class="header">
  <div class="brand"><span class="brand-dot"></span><span class="brand-name">LoomRinsePro</span></div>
  <div class="call">
    <span class="call-icon"><svg width="12" height="12" viewBox="0 0 24 24"><path fill="#fff" d="M6.6 10.8a15 15 0 0 0 6.6 6.6l2.2-2.2c.3-.3.7-.4 1-.2 1.1.4 2.3.6 3.6.6.6 0 1 .4 1 1V20c0 .6-.4 1-1 1A17 17 0 0 1 3 4c0-.6.4-1 1-1h3.5c.6 0 1 .4 1 1 0 1.3.2 2.5.6 3.6.1.3 0 .7-.2 1z"/></svg></span>
    Call Us Today <strong>+ 91 5550 123 456</strong>
  </div>
  <nav class="nav">
    <a class="active" href="#">Home</a><a href="#">About Us</a><a href="#">Services</a><a href="#">Testimonials</a><a href="#" style="border-right:0">Contact Us</a>
  </nav>
</header>

<div class="hero" role="img" aria-label="Modern living room with a lounge chair and a shaggy patterned rug on the floor"></div>
<div class="thumbs">
  <div class="thumb t1" role="img" aria-label="Water drop falling from a faucet"></div>
  <div class="thumb t2 current" role="img" aria-label="Shaggy rug in a living room"></div>
  <div class="thumb t3" role="img" aria-label="Worker cleaning a carpet"></div>
  <div class="thumb t4" role="img" aria-label="Residential house exterior"></div>
</div>

<section class="intro">
  <h1>Welcome to the Loom Rinse Pro</h1>
  <h2>There are many variations of passages of Lorem Ipsum available, but the have suffered alteration in some form, by injected humour,</h2>
  <p>There are many variations of passages of Lorem Ipsum available, but the majority have suffered alteration in some form, by injected humour, or randomised words which don't look even slightly believable. If you are going to use a passage of Lorem Ipsum, you need to be sure there isn't anything embarrassing hidden in the middle of text. All the Lorem Ipsum generators on the Internet tend to repeat predefined chunks as necessary, making this the first true generator on the Internet.</p>
  <p>It uses a dictionary of over 200 Latin words, combined with a handful of model sentence structures, to generate Lorem Ipsum which looks reasonable. The generated Lorem Ipsum is therefore always free from repetition, injected humour, or non-characteristic words etc.</p>
</section>

<aside class="services">
  <div class="services-rings"><span></span><span></span><span></span><span></span><span></span><span></span><span></span><span></span><span></span><span></span><span></span><span></span><span></span></div>
  <h3>Our Services</h3>
  <ul>
    <li>Rug Cleaning</li>
    <li>Upholstery Cleaning</li>
    <li>Residential and Commercial</li>
    <li>Carpet Cleanning</li>
    <li>Water Damage</li>
  </ul>
</aside>

<footer class="footer">
  <span class="marker"></span>
  <div class="footer-col" style="left:134px">
    <h4>Site Map</h4>
    <ul><li class="bullet">Home</li><li class="bullet">About Us</li><li class="bullet">Services</li><li class="bullet">Testimonials</li></ul>
  </div>
  <div class="footer-col" style="left:274px">
    <h4>Follow Us</h4>
    <ul>
      <li><span class="social-box"></span>Follow Us on Friendbook</li>
      <li><span class="social-box" style="background:#4d93c4"></span>Follow Us on Chirper</li>
      <li><span class="social-box" style="background:#d9772c"></span>Subscribe on RSS</li>
      <li><span class="social-box" style="background:#3f6f9a"></span>Linked UP</li>
    </ul>
  </div>
  <div class="footer-col" style="left:466px">
    <h4>Testimonials</h4>
    <p class="testimonial">It is a long established fact that a reader will be distracted by the readable content of a page when looking.</p>
    <p class="author">Martin Elroy Castell</p>
  </div>
  <div class="footer-col contact" style="left:713px">
    <h4>Contact Us</h4>
    <p><svg width="10" height="12" viewBox="0 0 10 14"><path fill="#ddd" d="M5 0a5 5 0 0 1 5 5c0 3.5-5 9-5 9S0 8.5 0 5a5 5 0 0 1 5-5zm0 3a2 2 0 1 0 0 4 2 2 0 0 0 0-4z"/></svg>Contrary to popular belief, Lorem Ipsum is not simply random text. It has roots in a piece of classical.</p>
    <p><svg width="10" height="12" viewBox="0 0 10 14"><rect x="1" y="0" width="8" height="14" rx="1.5" fill="#ddd"/><rect x="2.5" y="2" width="5" height="8" fill="#1f1f1f"/></svg>Phone : + 91 5550 123 456</p>
    <p><svg width="12" height="10" viewBox="0 0 12 9"><rect width="12" height="9" rx="1" fill="#ddd"/><path d="M0 0l6 5 6-5" stroke="#1f1f1f" fill="none"/></svg>E-mail : info@loomrinsepro.example</p>
  </div>
</footer>
</body>
</html>
```